Media Browser and player web application

I need to redesign a web application that enables to browse a media server (Tellavo) contents (images, audio, video) and play it in a web player.

Current implementation of the application can be seen at: http://www.tellavohub.example/content/demonstration-tellavo-pro-online-media-browser

This refresh is aiming to:
1) make the application simpler, based on typology (think Windows Metro style, VidSpire, Flickora); a simple fan concept is here: http://dex.lomarquin.example/tellavo/
2) make the application work on desktop as well as touch screen devices (ie no hover functionality, no pagination, large touch controls)
3) fast (remove unnecessary animations)
4) design with the app being responsive in mind

The attached UX designs show the basic flows in the application. Please note that the placement of controls (for example) is not set in stone and I welcome your input on the layout.

Ideally the default theme will be dark. Items' thumbnails will be square place holders, with images fit in them depending on the item icons' aspect ratio.

Also attaching the product's logo (Tellavo) and icon. The web application's name is ClipRover (or Tellavo ClipRover), so it should be included in the design (the UX designs include place holder Tellavo logo in the left top corner).

The main categories for each file type are (you will have to provide an icon for each of these):
- Audio: Albums, Artists, Album artists, Folders, Genres, Composers, Titles, Random music, Random albums, Last listened, Playlists, Online
- Image: Albums, Folders, Year, Month, Playlists, Online
- Video: Titles, Movies, Series, Folders, Last viewed, Last added, Genres, Actors, Directors, Producers, Release years, Playlists, Online
Updates

Target Market(s)

Mostly tech enthusiasts who want to stream their media over the internet to their devices.

Industry/Entity Type

Artists

Requirements
Must have
• Designs for all the provided UX designs
Touch-friendly web application design
High-res (Retina) assets
Light, type based Metro-like design
Nice to have
• Responsive web version
Dark and Light theme switching.
Should not have
• Chrome
Heavy graphics (eg backgrounds) that take time to load

```html
<!DOCTYPE html>
<html lang="en">
<head>
<meta charset="utf-8">
<title>Tellavo ClipRover – Login</title>
<link rel="stylesheet" href="https://fonts.googleapis.com/css2?family=Source+Sans+3:wght@400;600&display=swap">
<style>
  :root {
    --header-top: #e9f8fd;
    --header-bottom: #c5ecf8;
    --header-line: #ffffff;
    --nav-text: #111111;
    --nav-divider: #9fc9d6;
    --stage-bg: #2b3e54;
    --panel-bg: #1a2b40;
    --panel-edge: #3b5370;
    --panel-text: #ffffff;
    --input-bg: #ffffff;
    --input-border: #c9d3dc;
    --input-placeholder: #8a8f95;
    --button-top: #3a87c0;
    --button-bottom: #1d5f95;
    --button-border: #154a76;
    --footer-bg: #000000;
    --footer-text: #e8e8e8;
    --brand-mark: #f2e216;
    --brand-text: #111111;
  }
  * { box-sizing: border-box; margin: 0; padding: 0; }
  html, body {
    width: 1200px; height: 921px; overflow: hidden;
    font-family: "Source Sans 3", "Myriad Pro", sans-serif;
  }
  .page { position: relative; width: 1200px; height: 921px; overflow: hidden; }

  .stage {
    position: absolute; inset: 0 0 68px 0;
    background: var(--stage-bg);
  }

  .site-header {
    position: absolute; top: 0; left: 0; width: 1200px; height: 115px;
    background: linear-gradient(180deg, var(--header-top), var(--header-bottom));
    border-bottom: 1px solid var(--header-line);
  }
  .brand {
    position: absolute; left: 69px; top: 37px; height: 48px;
    display: flex; align-items: center; gap: 12px;
  }
  .brand-mark {
    width: 48px; height: 48px; border-radius: 6px; background: var(--brand-mark);
  }
  .brand-name {
    font-size: 56px; font-weight: 600; color: var(--brand-text); line-height: 1;
    letter-spacing: 1px;
  }
  .main-nav {
    position: absolute; right: 95px; top: 48px;
    display: flex; list-style: none; height: 40px; align-items: center;
  }
  .main-nav li {
    padding: 0 20px; height: 40px; display: flex; align-items: center;
    font-size: 17px; color: var(--nav-text); letter-spacing: 0.3px;
    border-left: 1px solid var(--nav-divider);
  }
  .main-nav li:first-child { border-left: none; }
  .main-nav li:last-child { padding-right: 0; }

  .login-panel {
    position: absolute; left: 347px; top: 306px; width: 507px; height: 221px;
    border-radius: 4px; border: 1px solid var(--panel-edge);
    background: var(--panel-bg);
    text-align: center;
  }
  .login-title {
    margin-top: 38px; font-size: 37px; font-weight: 400;
    color: var(--panel-text); line-height: 1;
  }
  .password-field {
    display: block; margin: 20px 0 0 69px; width: 365px; height: 40px;
    border: 1px solid var(--input-border); border-radius: 4px;
    background: var(--input-bg); padding: 0 15px;
    font: 400 17px "Source Sans 3", sans-serif;
  }
  .password-field::placeholder { color: var(--input-placeholder); }
  .login-button {
    display: block; margin: 13px auto 0; width: 103px; height: 41px;
    border: 1px solid var(--button-border); border-radius: 3px;
    background: linear-gradient(180deg, var(--button-top), var(--button-bottom));
    color: var(--panel-text); font: 400 18px "Source Sans 3", sans-serif;
  }

  .site-footer {
    position: absolute; left: 0; bottom: 0; width: 1200px; height: 68px;
    background: var(--footer-bg);
  }
  .copyright {
    position: absolute; left: 64px; top: 25px;
    font-size: 14px; color: var(--footer-text);
  }
  .social-links {
    position: absolute; right: 62px; top: 22px;
    display: flex; gap: 8px; list-style: none;
  }
  .social-links li {
    width: 24px; height: 24px; border-radius: 50%; background: var(--footer-text);
  }
</style>
</head>
<body>
<div class="page">
  <div class="stage" role="img" aria-label="Background photo area: meadow landscape with wind turbines and children flying a kite"></div>

  <header class="site-header">
    <div class="brand">
      <span class="brand-mark"></span>
      <span class="brand-name">Tellavo</span>
    </div>
    <ul class="main-nav">
      <li>HOME</li>
      <li>SERVICE</li>
      <li>DONWLOAD</li>
      <li>FORUM</li>
      <li>SUPPORT</li>
    </ul>
  </header>

  <form class="login-panel">
    <h1 class="login-title">Login into ClipRover</h1>
    <input class="password-field" type="password" placeholder="Password">
    <button class="login-button" type="button">Log In</button>
  </form>

  <footer class="site-footer">
    <p class="copyright">© 2013 Company Name.&nbsp; All right reserved</p>
    <ul class="social-links" aria-label="Social links">
      <li></li><li></li><li></li>
    </ul>
  </footer>
</div>
</body>
</html>
```